Food broker, trader, wholesaler, liquidator looking for a 5 pages website

Looking for a 5 pages website design. We are food brokers, traders, wholesaler and closeout buyer working with manufacturers, distributors, importers sell to retailers, food service operators and industrial (ingredients). We help market their products. We are a resource for those who need a solution in the distribution/selling/placement of food on the shelves, kitchens and pantries. Whether we open new accounts with new products or sell short dated inventory, we know where to go and get results.

Target Market(s)

Food manufacturers, food distributors, food brokers

Coding

Coded - Design and coding required

Number of Pages Required

4 page

Font styles to use
Serif

Requirements
Must have
• Food-food production-warehouse-Food packaging-people meeting-trucks-supermarket shelves-

```html
<!DOCTYPE html>
<html lang="en">
<head>
<meta charset="utf-8">
<title>Harborline Provisions</title>
<link href="https://fonts.googleapis.com/css2?family=Montserrat:wght@400;500;600&family=Lato:wght@400;700&display=swap" rel="stylesheet">
<style>
:root{
  --navy:#0d0c55;
  --navy-deep:#0a0a45;
  --ink:#222;
  --muted:#444;
  --white:#fff;
  --paper:#f6f7f5;
  --sea:#0b2436;
}
*{margin:0;padding:0;box-sizing:border-box}
html,body{width:1200px;height:3448px;overflow:hidden;background:var(--white)}
body{position:relative;font-family:'Lato',sans-serif;color:var(--ink)}
.abs{position:absolute}
h1,h2,h3,.nav a,.btn{font-family:'Montserrat',sans-serif}
a{text-decoration:none;color:inherit}

/* header */
.site-header{position:absolute;left:0;top:0;width:1200px;height:110px;border-bottom:1px solid #ddd}
.brand{position:absolute;left:176px;top:12px;display:flex;flex-direction:column;align-items:center;gap:6px}
.brand-dot{width:88px;height:64px;border-radius:50%;background:var(--navy)}
.brand-name{font-family:'Montserrat',sans-serif;font-weight:600;font-size:12px;color:var(--navy);letter-spacing:.3px}
.phone{position:absolute;right:174px;top:26px;font-family:'Montserrat',sans-serif;font-weight:500;font-size:20px;color:var(--navy);display:flex;align-items:center;gap:8px}
.nav{position:absolute;right:174px;top:80px;display:flex;gap:43px}
.nav a{font-size:14px;font-weight:500;color:#111}
.nav a.active{color:var(--navy)}

/* hero */
.hero{position:absolute;left:0;top:110px;width:1200px;height:580px;background:linear-gradient(90deg,#0a2d44 0%,#0c2a40 40%,#081c2e 100%)}
.hero-photo{position:absolute;left:0;top:0;width:680px;height:580px;background:linear-gradient(135deg,#163a62 0%,#1f5fa8 35%,#b8354e 60%,#1a3d63 100%);clip-path:polygon(0 45%,100% 10%,70% 100%,0 100%);opacity:.85}
.hero-title{position:absolute;left:701px;top:180px;font-size:41px;font-weight:600;line-height:45px;color:var(--white)}
.btn-outline-light{position:absolute;left:706px;top:292px;width:150px;height:42px;border:3px solid var(--white);border-radius:22px;color:var(--white);font-size:12px;font-weight:500;display:flex;align-items:center;justify-content:center;background:var(--navy)}
.dots{position:absolute;left:512px;top:478px;display:flex;gap:5px}
.dots span{width:40px;height:3px;background:var(--white)}
.dots span.off{background:transparent;border:1px solid var(--white)}

/* how it works */
.how{position:absolute;left:0;top:645px;width:1200px;height:573px;background:var(--navy);clip-path:polygon(0 40px,1200px 0,1200px 573px,0 573px);color:var(--white);overflow:hidden}
.how h2{position:absolute;top:72px;width:100%;text-align:center;font-size:31px;font-weight:500}
.lead{font-size:11px;line-height:22px;text-align:center}
.how .lead{position:absolute;top:124px;left:320px;width:560px;color:#eef}
.how svg{position:absolute;left:0;top:0}
.node-label{font-family:'Montserrat',sans-serif;font-size:12.5px;font-weight:500;fill:var(--white)}

/* about */
.about-photo{position:absolute;left:0;top:1218px;width:614px;height:502px;background:linear-gradient(120deg,#d8cdbd 0%,#9fb2c8 45%,#c5a886 100%)}
.play{position:absolute;left:306px;top:1422px}
.about{position:absolute;left:614px;top:1218px;width:586px;height:502px;background:var(--paper)}
.about h2{position:absolute;left:95px;top:82px;font-size:30px;font-weight:500;color:#111}
.about p{position:absolute;left:96px;top:130px;width:313px;font-size:11px;line-height:24px;text-align:justify;color:var(--muted)}
.btn-solid{position:absolute;left:95px;top:338px;width:122px;height:36px;border-radius:18px;background:var(--navy);color:var(--white);font-size:12.5px;font-weight:500;display:flex;align-items:center;justify-content:center}

/* specialized */
.special h2{position:absolute;top:1790px;width:1200px;text-align:center;font-size:30px;font-weight:500;color:#111}
.special .lead{position:absolute;top:1844px;left:320px;width:560px;color:#333}
.card{position:absolute;top:1919px;width:263px}
.card-photo{width:263px;height:163px;background:linear-gradient(135deg,#8a99ad,#c7a57e 60%,#4e5f78)}
.card h3{margin-top:30px;font-size:17px;font-weight:500;color:#111}
.card p{margin-top:10px;font-size:10.5px;line-height:20px;color:var(--muted);padding-left:2px}
.btn-outline{margin-top:16px;width:107px;height:32px;border:2px solid var(--navy);border-radius:16px;color:var(--navy);font-size:11.5px;font-weight:500;display:flex;align-items:center;justify-content:center}

/* what we do */
.what{position:absolute;left:0;top:2358px;width:1200px;height:404px;background:linear-gradient(90deg,#0b1e2e 0%,#1a2735 45%,#2a2226 75%,#101a26 100%);color:var(--white)}
.what h2{position:absolute;top:74px;width:100%;text-align:center;font-size:31px;font-weight:500}
.service{position:absolute;top:166px;width:260px}
.service h3{margin-top:12px;font-size:20px;font-weight:500}
.service p{margin-top:10px;font-size:12.5px;line-height:22px}

/* testimonial */
.quote-mark{position:absolute;left:578px;top:2820px}
.quote{position:absolute;left:265px;top:2888px;width:670px;text-align:center;font-size:13.5px;line-height:25px;color:#555}
.author{position:absolute;left:515px;top:2973px;display:flex;align-items:center;gap:14px}
.avatar{width:56px;height:56px;border-radius:50%;background:linear-gradient(135deg,#b7a896,#6c5f55)}
.author b{display:block;font-size:15px;font-weight:500;color:#111}
.author span{font-size:11.5px;font-weight:700;color:#333}
.pager{position:absolute;left:579px;top:3062px;display:flex;gap:6px}
.pager span{width:10px;height:10px;border-radius:50%;border:1px solid var(--navy)}
.pager span.on{background:var(--navy)}

/* footer */
.footer{position:absolute;left:0;top:3090px;width:1200px;height:358px;background:var(--navy);clip-path:polygon(0 36px,1200px 0,1200px 358px,0 358px);color:var(--white)}
.col{position:absolute;top:84px}
.col h4{font-family:'Montserrat',sans-serif;font-size:15px;font-weight:500;margin-bottom:16px}
.col li{list-style:none;font-size:11px;line-height:22.5px}
.contact-row{display:flex;gap:14px;font-size:11px;line-height:19px;margin-bottom:14px}
.foot-brand{position:absolute;left:862px;top:80px;width:160px;display:flex;flex-direction:column;align-items:center;gap:8px}
.foot-dot{width:94px;height:68px;border-radius:50%;background:var(--white)}
.foot-brand .brand-name{color:var(--white)}
.socials{display:flex;gap:14px;margin-top:14px}
.socials span{width:16px;height:16px;border-radius:50%;background:var(--white)}
.copyright{position:absolute;top:312px;width:100%;text-align:center;font-size:11px}
</style>
</head>
<body>

<header class="site-header">
  <div class="brand"><div class="brand-dot"></div><div class="brand-name">HARBORLINE PROVISIONS</div></div>
  <div class="phone">
    <svg width="20" height="20" viewBox="0 0 24 24"><path fill="#0d0c55" d="M6.6 10.8a15 15 0 0 0 6.6 6.6l2.2-2.2a1 1 0 0 1 1-.25 11.4 11.4 0 0 0 3.6.57 1 1 0 0 1 1 1V20a1 1 0 0 1-1 1A17 17 0 0 1 3 4a1 1 0 0 1 1-1h3.5a1 1 0 0 1 1 1c0 1.25.2 2.45.57 3.57a1 1 0 0 1-.25 1z"/></svg>
    PHONE:(555) 214-0387
  </div>
  <nav class="nav">
    <a class="active" href="#">HOME</a><a href="#">ABOUT US</a><a href="#">WHAT WE DO</a><a href="#">CONTACT</a><a href="#">GIVING BACK</a>
  </nav>
</header>

<section class="hero">
  <div class="hero-photo" role="img" aria-label="Aerial view of a container ship loaded with colourful containers cutting through deep blue sea"></div>
  <h1 class="hero-title">HARBORLINE<br>PROVISIONS</h1>
  <a class="btn-outline-light" href="#">GET STARTED</a>
  <div class="dots"><span></span><span></span><span class="off"></span><span></span></div>
</section>

<section class="how">
  <h2>HOW IT WORKS</h2>
  <p class="lead">Sed ut perspiciatis unde omnis iste natus error sit voluptatem accusantium doloremque laudantium, totam rem aperiam, eaque ipsa quae ab illo inventore veritatis et quasi architecto beatae vitae dicta sunt expli.</p>
  <svg width="1200" height="573" viewBox="0 0 1200 573" fill="none" stroke="#fff" stroke-width="1.5">
    <circle cx="600" cy="438" r="189"/>
    <circle cx="600" cy="438" r="86" stroke-width="2.5"/>
    <g fill="#0d0c55" stroke-width="1.5">
      <circle cx="416" cy="479" r="29"/>
      <circle cx="425" cy="373" r="29"/>
      <circle cx="499" cy="288" r="29"/>
      <circle cx="600" cy="251" r="29"/>
      <circle cx="701" cy="288" r="29"/>
      <circle cx="773" cy="373" r="29"/>
      <circle cx="777" cy="479" r="29"/>
    </g>
    <g stroke-width="1.3">
      <path d="M406 482h20M408 482a8 8 0 0 0 16 0M412 474l6-6"/>
      <path d="M415 381h20M418 381v-14l10 6M426 367l5-5"/>
      <path d="M488 298v-14l11-6 11 6v14zM493 298v-9h12v9"/>
      <path d="M590 246l10-6 10 6v12l-10 6-10-6zM590 246l10 6 10-6M600 252v12"/>
      <circle cx="696" cy="281" r="3"/><circle cx="707" cy="281" r="3"/><path d="M690 298v-8h12v8M702 298v-8h11v8"/>
      <path d="M760 380v-14h16v14zM776 370h8l3 5v5h-11M764 383a2 2 0 1 0 0 .1M781 383a2 2 0 1 0 0 .1"/>
      <path d="M765 475h24l-3 13h-18zM770 475l4-7M784 475l-4-7M772 479v6M777 479v6M782 479v6"/>
    </g>
    <g stroke-width="1.2">
      <path d="M420 449v-44M428 343l55-36M530 278l40-15M630 263l40 15M717 305l40 40M775 403v46"/>
    </g>
    <g stroke="none">
      <text class="node-label" x="600" y="208" text-anchor="middle">FOOD PACKAGING</text>
      <text class="node-label" x="449" y="292" text-anchor="end">WAREHOUSE</text>
      <text class="node-label" x="745" y="292">PEOPLE MEETING</text>
      <text class="node-label" x="372" y="377" text-anchor="end">FOOD PRODUCTION</text>
      <text class="node-label" x="815" y="377">TRUCKS</text>
      <text class="node-label" x="366" y="483" text-anchor="end">FOOD</text>
      <text class="node-label" x="821" y="483">SUPERMARKET SHELVES</text>
    </g>
  </svg>
</section>

<div class="about-photo" role="img" aria-label="Two warehouse colleagues checking a tablet beside a cardboard parcel"></div>
<svg class="play" width="92" height="92" viewBox="0 0 92 92"><circle cx="46" cy="46" r="43" fill="none" stroke="#fff" stroke-width="5"/><path d="M36 27v38l30-19z" fill="#fff"/></svg>
<section class="about">
  <h2>ABOUT US</h2>
  <p>Harborline Provisions works with food manufacturers, brand owners, distributors and wholesalers market their products. Retail, Food Service and Industrial ingredients. Founded in 2008, Harborline Provisions started with the distribution of gluten free products understanding the need to provide access to unique flavors and products for the celiac consumers. From this, we expanded into deli, dairy, groceries, frozen and beverages.</p>
  <a class="btn-solid" href="#">READ MORE</a>
</section>

<section class="special">
  <h2>WE ARE SPECIALIZED IN</h2>
  <p class="lead">Sed ut perspiciatis unde omnis iste natus error sit voluptatem accusantium doloremque laudantium, totam rem aperiam, eaque ipsa quae ab illo inventore veritatis et quasi architecto beatae vitae dicta sunt expli.</p>
  <article class="card" style="left:171px">
    <div class="card-photo" role="img" aria-label="Warehouse worker taping a cardboard box"></div>
    <h3>FOOD BROKERS</h3>
    <p>Lorem ipsum dolor sit amet, consectetur adipiscing elit, sed do eiusmod tempor incididunt ut labore et dolore magna aliqua.t enim ad minim veniam, quis nostrud exercitation ullamco lab</p>
    <a class="btn-outline" href="#">READ MORE</a>
  </article>
  <article class="card" style="left:468px">
    <div class="card-photo" role="img" aria-label="Traders working at a laptop among stock shelves"></div>
    <h3>TRADERS</h3>
    <p>Lorem ipsum dolor sit amet, consectetur adipiscing elit, sed do eiusmod tempor incididunt ut labore et dolore magna aliqua.t enim ad minim veniam, quis nostrud exercitation ullamco lab</p>
    <a class="btn-outline" href="#">READ MORE</a>
  </article>
  <article class="card" style="left:765px">
    <div class="card-photo" role="img" aria-label="Wholesale worker in a safety vest packing boxes"></div>
    <h3>WHOLESALER</h3>
    <p>Lorem ipsum dolor sit amet, consectetur adipiscing elit, sed do eiusmod tempor incididunt ut labore et dolore magna aliqua.t enim ad minim veniam, quis nostrud exercitation ullamco lab</p>
    <a class="btn-outline" href="#">READ MORE</a>
  </article>
</section>

<section class="what" role="img" aria-label="Dark aerial view of a cargo ship at sea behind the services">
  <h2>WHAT WE DO</h2>
  <div class="service" style="left:172px">
    <svg width="64" height="52" viewBox="0 0 64 52" fill="none" stroke="#fff" stroke-width="2.5"><path d="M2 2v48h60"/><path d="M8 46V26M18 46V20M28 46V30M38 46V22M48 46V14M58 46V8M8 24l10-8 10 12 10-10 10-6 10-6"/></svg>
    <h3>Sales &amp; Marketing</h3>
    <p>we connect food buyers and sellers through a dedicated approach.</p>
  </div>
  <div class="service" style="left:474px">
    <svg width="52" height="52" viewBox="0 0 52 52" fill="none" stroke="#fff" stroke-width="2"><path d="M4 2v42h46M8 46h42"/><path d="M10 40V10h6v30M20 40V16h6v24M30 40V22h6v24M40 40V28h6v12"/></svg>
    <h3>Trading</h3>
    <p>we purchase goods anywhere and ship them Nationwide and Export.</p>
  </div>
  <div class="service" style="left:790px">
    <svg width="52" height="52" viewBox="0 0 52 52" fill="none" stroke="#fff" stroke-width="2"><path d="M2 2v48M50 2v48M2 18h48M2 34h48M2 50h48"/><path d="M8 6h14v10H8zM28 6h14v10H28zM8 22h14v10H8zM28 22h14v10H28zM8 38h14v10H8zM28 38h14v10H28z"/></svg>
    <h3>Excess Inventory</h3>
    <p>we buy closeouts and excess inventory for prisons, outlet stores and discounters.</p>
  </div>
</section>

<svg class="quote-mark" width="44" height="36" viewBox="0 0 44 36"><path fill="#0d0c55" d="M2 36V20C2 8 9 2 18 0l2 4c-6 2-9 7-9 13h8v19zM26 36V20C26 8 33 2 42 0l2 4c-6 2-9 7-9 13h8v19z"/></svg>
<p class="quote">Curabitur iaculis tempus eros Curabitur vel mi sit amet magna malesuada ultrices Ut nisi erat fermentum vel congue id euismod in elit Curabitur iaculis tempus eros Curabitur vel mi sit amet magna malesuada ultrices Ut nisi erat fermentum vel congues Curabitur vel mi sit amet magna malesuada ultrices</p>
<div class="author"><div class="avatar" role="img" aria-label="Client portrait"></div><div><b>Dana Whitfield</b><span>Company Name</span></div></div>
<div class="pager"><span></span><span class="on"></span><span></span></div>

<footer class="footer">
  <div class="col" style="left:182px">
    <h4>Contact</h4>
    <div class="contact-row"><svg width="18" height="22" viewBox="0 0 18 22" fill="none" stroke="#fff" stroke-width="1.4"><path d="M9 21s7-7.5 7-12A7 7 0 0 0 2 9c0 4.5 7 12 7 12z"/><circle cx="9" cy="9" r="2.5"/></svg><div>48 Harbor Row,<br>Eastport Bay, 04631</div></div>
    <div class="contact-row"><svg width="22" height="22" viewBox="0 0 24 24" fill="none" stroke="#fff" stroke-width="1.4"><path d="M6.6 10.8a15 15 0 0 0 6.6 6.6l2.2-2.2 4.6 1.3V20A17 17 0 0 1 3 4h3.5l1.3 4.6z"/></svg><div>555 010 4421<br>555 010 7793</div></div>
    <div class="contact-row"><svg width="24" height="18" viewBox="0 0 24 18" fill="none" stroke="#fff" stroke-width="1.4"><rect x="1" y="1" width="22" height="16"/><path d="M1 1l11 9 11-9M1 17l8-8M23 17l-8-8"/></svg><div>info@example.com<br>founder@example.com</div></div>
  </div>
  <div class="col" style="left:448px">
    <h4>About Us</h4>
    <ul><li>Lorem ipsum dolo</li><li>Consectetur adipiscing elit.</li><li>Fusce eget leo tincid</li><li>Donec consequat</li><li>Praesent elementum</li><li>Jmauris posueret</li></ul>
  </div>
  <div class="col" style="left:679px">
    <h4>Information</h4>
    <ul><li>Lorem ipsum dolo</li><li>Consectetur adipiscing elit.</li><li>Fusce eec consequat</li><li>Praesent elementum</li><li>Jmauris posueret</li><li>Aenean a ex eu lectu</li></ul>
  </div>
  <div class="foot-brand">
    <div class="foot-dot"></div>
    <div class="brand-name">HARBORLINE PROVISIONS</div>
    <div class="socials"><span></span><span></span><span></span><span></span><span></span></div>
  </div>
  <p class="copyright">Copyright 2020 Harborline Provisions All Rights Reserved</p>
</footer>

</body>
</html>
```